Corporate Dinner Invitation – Bold, Professional Look with Subtle Arabic Flair

We are seeking a bold, professional invitation design for a VIP dinner event hosted by Tolarn during the BGLT Conference on Friday, July 18th. This will be used primarily for LinkedIn promotion and as a PDF invitation shared directly with physicians, so it must look clean and polished in portrait orientation.
The design should reflect a high-end corporate aesthetic while still being eye-catching. We’d like to see a very subtle Arabic or Moroccan-inspired design element — think minimal patterns or shapes worked lightly into the background or border. This flair should feel tasteful and restrained, not thematic or decorative. If you need some inspiration for the arabic/morrocan theme - please look up the Zaytuna Grove website (https://www.zaytunagr.com/).
Design Guidelines:
Portrait orientation only
Bold, clean, modern layout
Use of both Tolarn and KOR Spine LT brand colors preferred
Use of both Tolarn and KOR Spine LT logos (KOR Spine LT logo is a subsidiary of the Tolarn logo - so please make the Tolarn logo the larger of the two; they are both the same company - Tolarn owns KOR Spine LT).
Strong, readable typography that looks professional and commands attention
Design must work well as both a LinkedIn graphic and a standalone PDF
Visual tone: corporate, high-level, medical, innovative
Event Details:
Date: Friday, July 18th
Time: 8:00pm - 10:00pm EST
Location: Zaytuna Grove (318 SE Ocala Blvd, Miami, FL 33130)
Speakers: Gregory Lanke, MD; Warren Ostby, MD; Selu Varkin, MD (I am including headshots of each speaker - they need to be included on the invite - please remove the backgrounds in the headshot to make all of them uniform looking on the invite)
Final Deliverables:
High-res PDF
PNG or JPEG preview for LinkedIn
Editable source file (Canva, AI or InDesign)

```html
<!DOCTYPE html>
<html lang="en">
<head>
<meta charset="utf-8">
<title>Tolarn Dinner Invitation</title>
<link rel="stylesheet" href="https://fonts.googleapis.com/css2?family=Playfair+Display:wght@500;600&family=Bodoni+Moda:wght@400&family=Ubuntu:wght@500&family=Barlow+Condensed:wght@500&display=swap">
<style>
  :root {
    --gold: #e0c24a;
    --gold-line: #efe3a8;
    --green: #6db33f;
    --green-frame: #8cc63f;
    --navy: #1f2a55;
    --ink: #1d1d1d;
    --band: #e3e3de;
    --rule: #d9d9d6;
    --paper: #ffffff;
    --lattice-light: #fbfbfa;
    --lattice-tone: #ecece8;
  }
  * { margin: 0; padding: 0; box-sizing: border-box; }
  html, body { width: 960px; height: 1200px; overflow: hidden; background: var(--paper); }
  .invite { position: relative; width: 960px; height: 1200px; overflow: hidden; }
  .backdrop {
    position: absolute; inset: 0;
    background:
      radial-gradient(ellipse at 50% 100%, var(--lattice-tone) 0%, rgba(236,236,232,0) 60%),
      linear-gradient(90deg, var(--lattice-tone) 0%, var(--lattice-light) 12%, var(--lattice-light) 88%, var(--lattice-tone) 100%);
  }
  .outer-rule { position: absolute; left: 55px; top: 56px; width: 854px; height: 1092px; border: 1px solid var(--rule); background: var(--paper); }
  .band { position: absolute; left: 62px; top: 62px; width: 840px; height: 1081px; background: var(--band); }
  .panel { position: absolute; left: 80px; top: 80px; width: 804px; height: 1045px; background: var(--paper); }

  .brand { position: absolute; line-height: 1; font-family: "Barlow Condensed", sans-serif; font-weight: 500; white-space: nowrap; }
  .brand-main { left: 112px; top: 106px; font-size: 56px; color: var(--green); letter-spacing: 1px; }
  .brand-sub { right: 112px; top: 112px; font-size: 38px; color: var(--navy); letter-spacing: 1px; }

  .title {
    position: absolute; left: 0; width: 960px; text-align: center;
    font-family: "Playfair Display", serif; font-weight: 600; color: var(--gold); line-height: 1;
  }
  .title-dinner { top: 168px; font-size: 120px; letter-spacing: 2px; }
  .title-invitation { top: 291px; font-size: 89px; letter-spacing: 1px; }

  .section-label { position: absolute; height: 24px; }
  .section-label::before {
    content: ""; position: absolute; left: 0; right: 0; top: 15px; height: 1px; background: var(--gold-line);
  }
  .section-label span {
    position: relative; display: block; width: max-content; margin: 0 auto; padding: 0 4px;
    background: var(--paper); font-family: "Playfair Display", serif; font-weight: 600;
    font-size: 22px; color: var(--gold); line-height: 24px;
  }
  .label-date { left: 210px; width: 532px; top: 416px; }
  .label-location { left: 237px; width: 482px; top: 529px; }
  .label-speaker { left: 237px; width: 486px; top: 641px; }

  .detail {
    position: absolute; left: 0; width: 960px; text-align: center;
    font-family: "Bodoni Moda", serif; font-weight: 400; font-size: 22px; color: var(--ink); line-height: 1;
  }
  .detail-date { top: 464px; }
  .detail-location { top: 577px; }
  .detail .divider { display: inline-block; width: 1.5px; height: 24px; background: var(--ink); vertical-align: -4px; margin: 0 10px; }

  .speaker-photo {
    position: absolute; top: 718px; height: 298px; border: 1px solid var(--green-frame);
    background: linear-gradient(180deg, #f4f4f2 0%, #dfe2e6 100%);
  }
  .photo-1 { left: 121px; width: 181px; }
  .photo-2 { left: 386px; width: 187px; }
  .photo-3 { left: 655px; width: 187px; }

  .speaker-name {
    position: absolute; top: 1034px; width: 240px; text-align: center;
    font-family: "Ubuntu", sans-serif; font-weight: 500; font-size: 20px; color: var(--green); letter-spacing: 0.3px;
  }
  .name-1 { left: 84px; }
  .name-2 { left: 357px; }
  .name-3 { left: 625px; }
</style>
</head>
<body>
<main class="invite">
  <div class="backdrop" role="img" aria-label="Faint light-grey Moroccan lattice pattern background"></div>
  <div class="outer-rule"></div>
  <div class="band"></div>
  <div class="panel"></div>

  <div class="brand brand-main">TOLARN</div>
  <div class="brand brand-sub">KOR SPINE LT</div>

  <h1 class="title title-dinner">DINNER</h1>
  <div class="title title-invitation">INVITATION</div>

  <div class="section-label label-date"><span>DATE &amp; TIME</span></div>
  <p class="detail detail-date">Friday, July 18th<span class="divider"></span>8:00pm - 10:00pm EST</p>

  <div class="section-label label-location"><span>LOCATION</span></div>
  <p class="detail detail-location">Zaytuna Grove (318 SE Ocala Blvd, Miami, FL 33130)</p>

  <div class="section-label label-speaker"><span>SPEAKER</span></div>

  <div class="speaker-photo photo-1" role="img" aria-label="Headshot of Gregory Lanke, MD"></div>
  <div class="speaker-photo photo-2" role="img" aria-label="Headshot of Warren Ostby, MD"></div>
  <div class="speaker-photo photo-3" role="img" aria-label="Headshot of Selu Varkin, MD"></div>

  <p class="speaker-name name-1">Gregory Lanke, MD</p>
  <p class="speaker-name name-2">Warren Ostby, MD</p>
  <p class="speaker-name name-3">Selu Varkin, MD</p>
</main>
</body>
</html>
```